Tidewell Hypnotherapy 2017 DL Card Flyer

We would like a double sided DL Card Flyer design.

We are a professional Hypnotherapy Clinic looking for a fresh clean design.

Front of card is summary info and back of flyer is detailed text.

I have attached documents with text for the front (dl size hypno 1) and back (dl size hypno 2) of the card and an indicative style of layout.

There are logo files uploaded as well as one image file.

The colors we like are blue, white and yellow/gold.
Updates

please note: when using the 'bright steps bold change' image, please only use the top half of the image. The girl is not to be in the image, just the words and light bulb with the chalk underline. thanks.. Added Sunday, March 19, 2017

Industry/Entity Type

Health And Wellness

Requirements
Must have
• Note. I have misspelled the www.TidewellHypnotherapy.com.au (missing an 'o' in the attachments to the brief). My error. Please amend in your design submissions.

```html
<!DOCTYPE html>
<html lang="en">
<head>
<meta charset="utf-8">
<title>Tidewell Hypnotherapy – DL Card Flyer</title>
<link href="https://fonts.googleapis.com/css2?family=Open+Sans:ital,wght@0,400;0,600;0,700;0,800;1,400;1,600&family=Courgette&display=swap" rel="stylesheet">
<style>
  :root {
    --navy: #1d2668;
    --navy-deep: #141a4f;
    --gold: #e9d62c;
    --chalk: #333335;
    --white: #ffffff;
    --ink: #1f2a6e;
    --grey: #5b5f6e;
    --page: #e8e5e0;
  }
  * { box-sizing: border-box; margin: 0; padding: 0; }
  html, body { width: 1200px; height: 1200px; overflow: hidden; }
  body {
    background: var(--page);
    font-family: "Open Sans", Arial, sans-serif;
    display: flex;
    align-items: center;
    justify-content: center;
    gap: 60px;
  }
  .card {
    width: 471px;
    height: 1000px;
    position: relative;
    overflow: hidden;
    box-shadow: 0 6px 22px rgba(0,0,0,.18);
  }

  /* ---------- FRONT ---------- */
  .front { background: var(--navy); display: flex; flex-direction: column; }
  .front__header {
    background: var(--white);
    height: 160px;
    display: flex;
    align-items: center;
    justify-content: center;
    gap: 18px;
    padding-top: 10px;
  }
  .brand__dot {
    width: 86px; height: 86px; border-radius: 50%;
    background: var(--navy);
  }
  .brand__divider { width: 2px; height: 80px; background: var(--grey); }
  .brand__name {
    color: var(--ink);
    font-weight: 800;
    font-size: 27px;
    line-height: 1.1;
    text-transform: uppercase;
    letter-spacing: .5px;
  }
  .rule-pair { padding: 0 24px; }
  .rule-pair span { display: block; height: 3px; background: var(--navy-deep); margin-top: 5px; }
  .front__quote {
    padding: 26px 30px 30px;
    text-align: center;
    color: var(--white);
    font-family: "Courgette", cursive;
    font-size: 25px;
    line-height: 1.25;
  }
  .front__chalkboard {
    height: 270px;
    background: radial-gradient(ellipse at 50% 55%, #4a4a3a 0%, var(--chalk) 60%);
  }
  .programs { padding: 30px 36px 0; color: var(--white); flex: 1; display: flex; flex-direction: column; }
  .programs__title { font-weight: 700; font-size: 19px; text-align: center; margin-bottom: 4px; }
  .programs__rule { height: 2px; background: var(--white); margin: 6px 20px 18px; }
  .programs__list { list-style: none; }
  .programs__list li {
    font-size: 19px; line-height: 1.45;
    padding-left: 34px; position: relative;
  }
  .programs__list li::before {
    content: ""; position: absolute; left: 4px; top: 9px;
    width: 13px; height: 11px; background: var(--gold); transform: skewX(-20deg);
  }
  .contact { margin-top: 26px; text-align: center; position: relative; }
  .contact__line { position: absolute; top: 18px; left: -36px; right: -36px; height: 2px; background: var(--white); }
  .contact__ribbon {
    position: relative; display: inline-block;
    background: var(--white); color: var(--ink);
    font-weight: 800; font-size: 19px; letter-spacing: 1px;
    padding: 5px 30px; text-transform: uppercase;
    clip-path: polygon(0 0,100% 0,92% 50%,100% 100%,0 100%,8% 50%);
  }
  .contact__phone {
    display: flex; align-items: center; justify-content: center; gap: 14px;
    font-weight: 700; font-size: 26px; margin-top: 12px; letter-spacing: 1px;
  }
  .contact__dot { width: 32px; height: 32px; border-radius: 50%; background: var(--white); }
  .front__footer { margin-top: auto; }
  .front__footer .rule-pair span { background: var(--white); }
  .front__web {
    background: var(--white); color: var(--ink);
    font-weight: 700; font-size: 19px; text-align: center;
    padding: 14px 0 16px; margin-top: 14px;
  }

  /* ---------- BACK ---------- */
  .back {
    background: radial-gradient(ellipse at 50% 40%, #242e78 0%, var(--navy-deep) 100%);
    color: var(--white);
    padding: 30px 22px 26px;
    display: flex; flex-direction: column;
  }
  .back__title {
    display: flex; align-items: center; gap: 12px; justify-content: center;
    font-weight: 700; font-size: 21px; font-variant: small-caps; letter-spacing: 1px;
    margin-bottom: 14px;
  }
  .back__title::before, .back__title::after {
    content: ""; height: 3px; width: 80px; background: var(--gold); border-radius: 2px;
  }
  .program { margin-bottom: 14px; }
  .program__name {
    display: inline-block;
    background: var(--gold); color: var(--navy-deep);
    font-weight: 700; font-size: 13px; text-transform: uppercase;
    padding: 4px 18px; border-radius: 14px; margin-bottom: 7px;
  }
  .program__text { font-size: 12.6px; line-height: 1.45; text-align: justify; }
  .program__sessions { color: var(--gold); font-style: italic; font-weight: 600; font-size: 12.6px; }
  .back__note {
    margin-top: auto;
    border: 2px solid rgba(255,255,255,.7);
    padding: 14px 18px;
    font-style: italic; font-size: 13px; line-height: 1.5; text-align: center;
  }
</style>
</head>
<body>

<section class="card front" aria-label="Flyer front">
  <header class="front__header">
    <div class="brand__dot"></div>
    <div class="brand__divider"></div>
    <div class="brand__name">Tidewell<br>Hypnotherapy</div>
  </header>
  <div class="rule-pair"><span></span><span></span></div>
  <p class="front__quote">“There is nothing more important than good health”</p>
  <div class="front__chalkboard" role="img" aria-label="Chalkboard illustration: lit light bulb with dashed arrow and chalk words bright steps bold change"></div>
  <div class="programs">
    <h2 class="programs__title">Professional Hypnosis Therapy Programs</h2>
    <div class="programs__rule"></div>
    <ul class="programs__list">
      <li>Weight Loss (Virtual Gastric Band)</li>
      <li>Sugar Addiction</li>
      <li>Quit Smoking</li>
      <li>Chronic Fatigue &amp; Chronic Pain Relief</li>
      <li>Stress Relief &amp; Deep Relaxation</li>
    </ul>
    <div class="contact">
      <div class="contact__line"></div>
      <span class="contact__ribbon">Call Us</span>
      <div class="contact__phone"><span class="contact__dot"></span>1300 555 014</div>
    </div>
  </div>
  <footer class="front__footer">
    <div class="rule-pair"><span></span><span></span></div>
    <div class="front__web">www.TidewellHypnotherapy.com.au</div>
  </footer>
</section>

<section class="card back" aria-label="Flyer back">
  <h2 class="back__title">Program Details</h2>

  <article class="program">
    <h3 class="program__name">Weight Loss Program (Virtual Gastric Band)</h3>
    <p class="program__text">Achieve long term weight loss without dieting. Whether losing 3kg or 30kg, we'll help you become the shape and size you want to be. Our internationally Accredited Program is proven to be 95% effective in clinical trials.</p>
    <p class="program__sessions">Number of Sessions: 6+</p>
  </article>

  <article class="program">
    <h3 class="program__name">Sugar Addiction Program</h3>
    <p class="program__text">Excess sugar intake can lead to obesity, Type 2 Diabetes and tooth decay. The habit of reaching for soft drinks, chocolate, sweets, cakes and biscuits can be hard to break. By rewiring your subconscious habits, our Program puts you back in control.</p>
    <p class="program__sessions">Number of Sessions: 3+</p>
  </article>

  <article class="program">
    <h3 class="program__name">Quit Smoking Program</h3>
    <p class="program__text">The facts speak for themselves. You are 10 times more likely to quit smoking for good using hypnotherapy. Expect to be a non smoker after completing the first session of our Program. (12 Month Guarantee)</p>
    <p class="program__sessions">Number of Sessions: 2</p>
  </article>

  <article class="program">
    <h3 class="program__name">Chronic Fatigue &amp; Chronic Pain Relief Program</h3>
    <p class="program__text">Chronic Fatigue, Fibromyalgia and Chronic Musculoskeletal Pain are diseases of modern living. The symptoms of fatigue and pain are very real, however the cause is usually emotional, and is generally hidden beyond our conscious awareness. Our Program comprises Education and Hypnosis to help you regain your health, your self esteem, your friends and your life, all in a manageable timeframe.</p>
    <p class="program__sessions">Number of Sessions: 6+</p>
  </article>

  <article class="program">
    <h3 class="program__name">Stress Relief &amp; Deep Relaxation Program</h3>
    <p class="program__text">Our Program gently uncovers the true source of your stress, and helps you reconnect to a natural inner calm. We teach you self hypnosis so that you have the tools to continue your experience.</p>
    <p class="program__sessions">Number of Sessions: 3+</p>
  </article>

  <p class="back__note">All Programs include take home CD's personally recorded by our therapists, using advanced hypnotic techniques.</p>
</section>

</body>
</html>
```